Organic Food Producer Needs Business Card

We need an attractive business card that is both trendy and professional. We are a FQIB, Non Gmo Certified organic producer of coconut oil, coconut flour and additional cacao products. We produce some of the world's purest coconut oil and coconut oil derived products in the world.
We take pride in the purity of our products and the transparency with which we create our products. Use of FQIB Organic and Non GMO logos is acceptable and preferred. The final design would reflect our values for purity and the natural state of our products.
The business card should include: job title, email address, phone number and facebook, twitter, instagram tag.
Don't be afraid to get creative! I have attached some of our packaging design in JPG format as well as our logo. The jpgs dont display the colors correctly in chrome but they will display correctly if you DL and open them in photoshop.
Target Market(s)
Cards likely to be used in organic food industry events for people such as buyers, trade show reps, etc... but also store owners and people casually interested in.
The company's target market :
Primary:
Women - 22-65. Women typically hold the household budget and make the purchasing decisions at the supermarket. They are interested in quality healthy and beauty products at a good value. Organic, fair trade, artisanally made are all important attributes of brands they purchase. They try to maintain a healthy lifestyle through proper eating, exercise and work/life balance.
Secondary:
Men - 44% of American adults are single so it is important to note that men will also be a key target audience. And they too are concerned and passionate about organic, fair trade, artisanally made, good value and living a healthy lifestyle.
Tertiary:
Health & Wellness Professionals (Nutritionists, Doctors, etc) Coconut is highly nutritional and more and more, it is being recommended as part of a healthy diet by professionals. We should keep this audience in mind as well, particularly when we build a website with useful resources such as the company’s high standards, the health benefits of coconut, nutrition info and recipes.
Industry/Entity Type
Business
Requirements
Must have
- Pretty open minded about creativity and variety, I do like the color palettes in the labeling files provided... but it is not a deal breaker to vary from this.
Should be visually impacting.
Nice to have
- Would like to have some creative use of raised lettering or detail.
Should not have
- Although the company is based in the caribbean, we are not looking for an overly ethnic caribbean feel.
You should open the attached files in photoshop, as they seem to distort the color in a web browser.

```html
<!DOCTYPE html>
<html lang="en">
<head>
<meta charset="utf-8">
<title>Clear Grove – Business Card</title>
<link href="https://fonts.googleapis.com/css2?family=Open+Sans:wght@400;600&display=swap" rel="stylesheet">
<style>
  :root {
    --page: #ffffff;
    --husk-dark: #2e2013;
    --husk-mid: #5a4128;
    --husk-light: #7a5a38;
    --flesh-light: #eeece4;
    --flesh-mid: #cfccc2;
    --flesh-dark: #a9a69b;
    --band: #3f2410;
    --cream: #f4e4c3;
    --peach: #f0cf9f;
    --white: #ffffff;
    --teal: #1c92ad;
  }
  * { box-sizing: border-box; margin: 0; padding: 0; }
  html, body {
    width: 1200px; height: 1000px; overflow: hidden;
    background: var(--page);
    font-family: "Open Sans", Arial, sans-serif;
  }
  .canvas { position: relative; width: 1200px; height: 1000px; }
  .card {
    position: absolute; left: 302px; width: 578px; height: 356px;
    overflow: hidden;
    box-shadow: 3px 4px 6px rgba(0,0,0,0.35);
  }
  .card--front { top: 91px; }
  .card--back { top: 530px; }

  .husk-photo {
    position: absolute; inset: 0;
    background:
      radial-gradient(ellipse at 45% 55%, var(--husk-light) 0%, var(--husk-mid) 45%, var(--husk-dark) 100%);
  }
  .flesh-photo {
    position: absolute; inset: 0;
    background:
      radial-gradient(ellipse at 50% 60%, var(--flesh-light) 0%, var(--flesh-mid) 60%, var(--flesh-dark) 100%);
  }

  .brand {
    position: absolute; display: flex; align-items: center; gap: 12px;
    color: var(--cream); font-weight: 600; line-height: 1; white-space: nowrap;
  }
  .brand__dot { border-radius: 50%; background: var(--teal); flex: none; }
  .card--front .brand { left: 50%; top: 50%; transform: translate(-50%, -50%); font-size: 44px; }
  .card--front .brand__dot { width: 40px; height: 40px; }

  .band { position: absolute; left: 0; top: 92px; width: 578px; height: 151px; }
  .band svg { display: block; }
  .card--back .brand { left: 56px; top: 150px; font-size: 28px; gap: 9px; }
  .card--back .brand__dot { width: 28px; height: 28px; }

  .divider { position: absolute; left: 307px; top: 138px; width: 1px; height: 68px; background: var(--peach); }
  .contact { position: absolute; left: 331px; top: 131px; color: var(--peach); }
  .contact__name { font-size: 15.5px; letter-spacing: 0.2px; line-height: 20px; }
  .contact__title { font-size: 9.5px; color: var(--cream); line-height: 14px; }
  .contact__phone { font-size: 17px; color: var(--white); margin-top: 8px; line-height: 22px; }
  .contact__email { font-size: 12.5px; line-height: 17px; }

  .social { position: absolute; top: 288px; left: 213px; display: flex; gap: 20px; }
  .social__item { width: 36px; height: 36px; border-radius: 50%; background: var(--band); }
</style>
</head>
<body>
<div class="canvas">

  <section class="card card--front">
    <div class="husk-photo" role="img" aria-label="Close-up photograph of a brown fibrous coconut husk"></div>
    <div class="brand"><span class="brand__dot"></span>clear grove</div>
  </section>

  <section class="card card--back">
    <div class="flesh-photo" role="img" aria-label="Close-up photograph of white coconut flesh inside the shell"></div>
    <div class="band">
      <svg width="578" height="151" viewBox="0 0 578 151" aria-hidden="true">
        <path fill="var(--band)" d="M0 6 L40 4 L90 7 L150 3 L220 6 L300 2 L370 6 L450 3 L520 7 L578 4 L578 147 L510 144 L430 149 L350 145 L270 150 L190 146 L110 149 L50 145 L0 148 Z"/>
      </svg>
    </div>
    <div class="brand"><span class="brand__dot"></span>clear grove</div>
    <div class="divider"></div>
    <div class="contact">
      <p class="contact__name">Mirela Santos</p>
      <p class="contact__title">Director</p>
      <p class="contact__phone">0715550182</p>
      <p class="contact__email">santos@mailbox.net</p>
    </div>
    <div class="social" aria-label="Social media">
      <span class="social__item"></span>
      <span class="social__item"></span>
      <span class="social__item"></span>
    </div>
  </section>

</div>
</body>
</html>
```